Business Card Design

We are a residential half way house for the addict ,the alcoholic and dual diagnosed in recovery.
i house both men and woman age 18+

Industry/Entity Type

Residential

```html
<!DOCTYPE html>
<html lang="en">
<head>
<meta charset="utf-8">
<title>Meadowlight Family Sober House – Business Card</title>
<link rel="stylesheet" href="https://fonts.googleapis.com/css2?family=Dancing+Script:wght@500&family=Quicksand:wght@500;700&display=swap">
<style>
  :root {
    --backdrop: #ece6dc;
    --card: #2f2f30;
    --card-light: #3a3a3b;
    --card-band: #262627;
    --ink: #ffffff;
    --red: #c8203a;
    --orange: #e4541c;
    --yellow: #ecb107;
    --green: #5aab2c;
    --teal: #14a0a8;
    --stripe-orange: #ee7a1a;
    --stripe-yellow: #f2c40c;
  }
  * { box-sizing: border-box; margin: 0; padding: 0; }
  html, body {
    width: 1200px; height: 800px; overflow: hidden;
    background: var(--backdrop);
  }
  .canvas {
    position: relative; width: 1200px; height: 800px;
  }
  .card {
    position: absolute; left: 345px; width: 510px; height: 290px;
    border-radius: 12px; overflow: hidden;
    background: radial-gradient(ellipse at 50% 30%, var(--card-light), var(--card) 70%);
    box-shadow: 0 6px 18px rgba(0,0,0,.25);
    color: var(--ink);
  }
  .card--front { top: 75px; }
  .card--back { top: 430px; }

  .brand-name {
    font-family: "Dancing Script", cursive;
    font-weight: 500; line-height: 1.05; color: var(--ink);
  }
  .card--front .brand-name {
    position: absolute; top: 82px; left: 0; right: 0;
    text-align: center; font-size: 42px;
  }
  .rainbow-stripe {
    position: absolute; left: 0; right: 0; top: 193px; height: 14px; display: flex;
  }
  .rainbow-stripe span { flex: 1; }
  .rainbow-stripe .s1 { background: var(--red); flex: 1.1; }
  .rainbow-stripe .s2 { background: var(--stripe-orange); }
  .rainbow-stripe .s3 { background: var(--stripe-yellow); }
  .rainbow-stripe .s4 { background: var(--green); }
  .rainbow-stripe .s5 { background: var(--teal); flex: 1.1; }
  .lower-band {
    position: absolute; left: 0; right: 0; top: 207px; bottom: 0;
    background: var(--card-band);
  }
  .address {
    position: absolute; left: 0; right: 0; top: 237px; text-align: center;
    font-family: "Quicksand", sans-serif; font-weight: 500; font-size: 16px;
  }

  .card--back .brand-name {
    position: absolute; top: 105px; left: 22px; font-size: 31px;
    text-align: center; width: 240px;
  }
  .contact-panel {
    position: absolute; right: 0; top: 10px; width: 245px;
    font-family: "Quicksand", sans-serif;
  }
  .contact-row {
    display: flex; align-items: center; position: relative;
  }
  .contact-row .icon {
    flex: 0 0 58px; align-self: stretch; display: flex; align-items: center; justify-content: center;
    background: rgba(0,0,0,.08);
  }
  .contact-row .icon svg { width: 22px; height: 22px; fill: var(--ink); }
  .contact-row .details {
    padding: 0 10px 0 14px; font-size: 14px; font-weight: 500; line-height: 1.15;
    min-width: 0; white-space: nowrap;
  }
  .row--person { background: var(--red); height: 95px; }
  .row--phone { background: var(--orange); height: 55px; }
  .row--fax { background: var(--yellow); height: 52px; }
  .row--email { background: var(--green); height: 56px; }
  .person-name { font-weight: 700; font-size: 16px; letter-spacing: .5px; text-transform: uppercase; }
  .person-role { font-size: 14px; }
  .row--email .details { font-size: 13px; }
</style>
</head>
<body>
<main class="canvas">
  <section class="card card--front" aria-label="Card front">
    <h1 class="brand-name">Meadowlight Family<br>Sober House Inc.</h1>
    <div class="rainbow-stripe"><span class="s1"></span><span class="s2"></span><span class="s3"></span><span class="s4"></span><span class="s5"></span></div>
    <div class="lower-band"></div>
    <p class="address">2718 Palmetto Rd. Harbor Springs, Fla 33400</p>
  </section>

  <section class="card card--back" aria-label="Card back">
    <h2 class="brand-name">Meadowlight Family<br>Sober House Inc.</h2>
    <div class="contact-panel">
      <div class="contact-row row--person">
        <div class="icon"><svg viewBox="0 0 24 24"><circle cx="12" cy="8" r="5"/><path d="M2 23c0-6 4.5-9 10-9s10 3 10 9z"/></svg></div>
        <div class="details">
          <div class="person-name">Renata Vidal</div>
          <div class="person-role">Owner<br>15 years in recovery</div>
        </div>
      </div>
      <div class="contact-row row--phone">
        <div class="icon"><svg viewBox="0 0 24 24"><path d="M2 9c0-3 5-5 10-5s10 2 10 5v2h-5V8.5c-3-1-7-1-10 0V11H2z"/><path d="M6 12h12l3 9H3z"/></svg></div>
        <div class="details">(555) 014-2210<br>(555) 014-2211</div>
      </div>
      <div class="contact-row row--fax">
        <div class="icon"><svg viewBox="0 0 24 24"><rect x="6" y="2" width="12" height="6"/><path d="M2 9h20v9h-4v-4H6v4H2z"/><rect x="7" y="15" width="10" height="7"/></svg></div>
        <div class="details">Fax (555) 014-7782</div>
      </div>
      <div class="contact-row row--email">
        <div class="icon"><svg viewBox="0 0 24 24"><path d="M2 5h20v14H2z" fill="none" stroke="#fff" stroke-width="2"/><path d="M2 5l10 8 10-8" fill="none" stroke="#fff" stroke-width="2"/></svg></div>
        <div class="details">renatavidal@mail.com</div>
      </div>
    </div>
  </section>
</main>
</body>
</html>
```